Packaging for a Kids' Drink Mix

Brightly Our Finest produces a powdered drink mix for children call Moonrocket Meals for Kids, An organic drink mix which provides 100% of the recommended daily allowance of fruits, veggies and protein. The label must attract an American audience. We would like to use kids' colors, fonts and ideas. It should communicate fun and health using our Brightly Our Finest logo, bar code and nutritional data.

I will supply barcode.
Updates

Very disappointed writhe the designs I received.

Target Market(s)

Kids and Moms in the US Health and Wellness Niche

Industry/Entity Type

Health And Wellness

Font styles to use
Sans Serif

Colors

Designer to choose colors to be used in the design.

Requirements
Must have
• Brightly Our Finest LOGO, MoonRocket Drink Mix for Kids, 100% of the RDA for Fruits, Veggies and Protein, Organic, Non-GMO, USA Grown and Produced.

```html
<!DOCTYPE html>
<html lang="en">
<head>
<meta charset="utf-8">
<title>Moonrocket Meals for Kids – Drink Mix Label</title>
<link rel="stylesheet" href="https://fonts.googleapis.com/css2?family=Fredoka:wght@500;600&family=Open+Sans:wght@400;700&display=swap">
<style>
  :root {
    --page: #ffffff;
    --label-rim: #eeb53a;
    --label-face: #f1be45;
    --label-line: #ffffff;
    --title-green: #1f6b3b;
    --subtitle-green: #3a6a1f;
    --band-olive: #899a3b;
    --band-text: #f6f08c;
    --claims-panel: #f5f07a;
    --claims-text: #111111;
    --stamp-olive: #8d8b2f;
    --stamp-ring: #a9a641;
    --cert-blue: #a9c7e6;
    --cert-navy: #1f4e9a;
    --brand-green: #6f9b4b;
    --fruit-yellow: #f4e25a;
    --fruit-orange: #f39a2d;
    --fruit-red: #d6262b;
    --fruit-green: #b9d77a;
  }
  * { margin: 0; padding: 0; box-sizing: border-box; }
  html, body {
    width: 1200px; height: 1200px; overflow: hidden;
    background: var(--page);
  }
  .stage {
    position: absolute; left: 0; top: 0;
    width: 1000px; height: 1000px;
    transform: scale(1.2); transform-origin: 0 0;
  }
  .label-shape { position: absolute; inset: 0; }
  .product-title {
    position: absolute; left: 0; top: 0; width: 1000px; height: 1000px;
    font-family: "Fredoka", "Trebuchet MS", sans-serif;
  }
  .product-title .title-arc { font-size: 35px; font-weight: 600; fill: var(--title-green); letter-spacing: 0.5px; }
  .product-title .title-kids { font-size: 40px; font-weight: 600; fill: var(--subtitle-green); }
  .fruit-art {
    position: absolute; left: 350px; top: 328px; width: 320px; height: 170px;
    border-radius: 50% 50% 0 0 / 80% 80% 0 0;
    background: linear-gradient(100deg, var(--fruit-green) 0%, var(--fruit-orange) 45%, var(--fruit-red) 75%, var(--fruit-yellow) 100%);
    opacity: 0.9;
  }
  .flavor-band {
    position: absolute; left: 327px; top: 503px; width: 361px; height: 53px;
    background: var(--band-olive);
    border-radius: 5px;
    outline: 5px solid var(--label-line);
    display: flex; align-items: center; justify-content: center;
    text-align: center;
    font-family: "Fredoka", "Trebuchet MS", sans-serif; font-weight: 500;
    font-size: 19px; line-height: 22px; color: var(--band-text);
    letter-spacing: 0.3px;
  }
  .claims-panel {
    position: absolute; left: 350px; top: 640px; width: 316px; height: 246px;
    background: var(--claims-panel); border-radius: 8px;
  }
  .claims-list {
    list-style: none; position: absolute; right: 9px; top: -2px;
    text-align: right;
    font-family: "Open Sans", Arial, sans-serif; font-weight: 700;
    font-size: 21px; line-height: 44px; color: var(--claims-text);
    letter-spacing: -0.3px;
  }
  .cert-mark {
    position: absolute; left: 6px; top: 178px; width: 140px; height: 63px;
    background: var(--cert-blue);
  }
  .cert-mark::after {
    content: ""; position: absolute; right: 0; top: 0; width: 70px; height: 63px;
    background: var(--cert-navy);
  }
  .brand-mark {
    position: absolute; left: 150px; top: 228px;
    display: flex; align-items: center; gap: 4px;
    font-family: "Open Sans", Arial, sans-serif; font-weight: 400;
    font-size: 10.5px; letter-spacing: 1px; text-transform: uppercase;
    color: var(--brand-green); white-space: nowrap;
  }
  .brand-mark .brand-dot {
    width: 7px; height: 7px; border-radius: 50%; background: var(--brand-green);
  }
</style>
</head>
<body>
<main class="stage">
  <svg class="label-shape" viewBox="0 0 1000 1000" width="1000" height="1000" aria-hidden="true">
    <path d="M362 58 H653 L680 85 V925 L653 952 H362 L335 925 V85 Z"
          fill="var(--label-rim)" stroke="var(--label-rim)" stroke-width="22" stroke-linejoin="round"/>
    <path d="M372 73 H643 L665 95 V915 L643 937 H372 L350 915 V95 Z"
          fill="var(--label-face)" stroke="var(--label-line)" stroke-width="4" stroke-linejoin="round"/>
    <g class="organic-seal">
      <circle cx="608" cy="140" r="50" fill="var(--stamp-ring)"/>
      <circle cx="608" cy="140" r="40" fill="none" stroke="var(--stamp-olive)" stroke-width="4"/>
      <circle cx="608" cy="140" r="31" fill="var(--stamp-olive)"/>
    </g>
  </svg>

  <svg class="product-title" viewBox="0 0 1000 1000" width="1000" height="1000">
    <defs>
      <path id="title-curve" d="M368 278 Q512 160 662 278"/>
    </defs>
    <text class="title-arc"><textPath href="#title-curve" startOffset="50%" text-anchor="middle">Moonrocket Meals</textPath></text>
    <text class="title-kids" x="511" y="299" text-anchor="middle">for Kids</text>
  </svg>

  <div class="fruit-art" role="img" aria-label="Illustration of grapes, an orange, cherries and a strawberry with a juice splash"></div>

  <div class="flavor-band">MoonRocket Drink Mix<br>for Kids</div>

  <section class="claims-panel">
    <ul class="claims-list">
      <li>100% of the RDA for Fruits</li>
      <li>Veggies and Protein</li>
      <li>Non-GMO</li>
      <li>USA Grown and Produced</li>
    </ul>
    <div class="cert-mark" aria-hidden="true"></div>
    <div class="brand-mark"><span class="brand-dot"></span>Brightly Our Finest</div>
  </section>
</main>
</body>
</html>
```